Business Card Design Project

New business cards that encompass our new logo.
Looking for -
Name, Title, Cell Phone, Email, Address (2 lines), Main Phone, Fax, and website.
Reason: I don't like the graphics used to show phone, fax, cell, email, web, and address.....
I like the double sided cards with logo's on the back. I do not like the logos for phone, fax, cell, address, email, or web.

```html
<!DOCTYPE html>
<html lang="en">
<head>
<meta charset="utf-8">
<title>Northwind Supply – Business Card</title>
<link href="https://fonts.googleapis.com/css2?family=Lato:wght@400;700;900&display=swap" rel="stylesheet">
<style>
  :root {
    --navy: #15307a;
    --red: #c8262c;
    --white: #ffffff;
    --backdrop: #e9e7e3;
  }
  * { box-sizing: border-box; margin: 0; padding: 0; }
  html, body {
    width: 1200px; height: 900px; overflow: hidden;
    background: var(--backdrop);
    font-family: "Lato", sans-serif;
  }
  .card {
    position: absolute; left: 100px; top: 165px;
    width: 1000px; height: 571px;
    background: var(--white);
    border-radius: 28px; overflow: hidden;
    box-shadow: 0 10px 30px rgba(0,0,0,.18);
    color: var(--navy);
  }
  .holder { position: absolute; right: 60px; top: 50px; text-align: right; }
  .holder-name { color: var(--red); font-size: 30px; font-weight: 400; letter-spacing: .5px; line-height: 36px; }
  .holder-title { font-size: 24px; font-weight: 700; line-height: 30px; margin-top: 2px; }
  .brand {
    position: absolute; left: 60px; top: 200px;
    display: flex; align-items: center; gap: 14px;
  }
  .brand-mark { width: 20px; height: 20px; background: var(--red); flex: none; }
  .brand-name { font-size: 44px; line-height: 52px; font-weight: 900; color: var(--navy); letter-spacing: 1px; white-space: nowrap; }
  .phones {
    position: absolute; right: 60px; top: 258px;
    list-style: none; text-align: right;
  }
  .phones li { font-size: 28px; line-height: 36px; font-weight: 400; white-space: nowrap; }
  .online {
    position: absolute; left: 60px; top: 352px; list-style: none;
  }
  .online li { font-size: 28px; line-height: 36px; font-weight: 700; white-space: nowrap; }
  .address-band {
    position: absolute; left: 0; right: 0; bottom: 0; height: 118px;
    background: var(--navy); color: var(--white);
    display: flex; align-items: center; justify-content: center;
    font-size: 28px; font-weight: 700; letter-spacing: .3px;
  }
</style>
</head>
<body>
  <article class="card">
    <header class="holder">
      <p class="holder-name">DANA ELLIS</p>
      <p class="holder-title">Managing Director</p>
    </header>

    <div class="brand">
      <span class="brand-mark"></span>
      <span class="brand-name">NORTHWIND SUPPLY</span>
    </div>

    <ul class="phones">
      <li>+123 456 7890</li>
      <li>+111 222 3333</li>
      <li>+000 000 0000</li>
    </ul>

    <ul class="online">
      <li>danaellis@mail.com</li>
      <li>www.northwindsupply.com</li>
    </ul>

    <footer class="address-band">Building No.1, Street Name, City, State, Zip</footer>
  </article>
</body>
</html>
```